Glow With Mira, Lifting Your Inner Radiance

Selling lipglosses, adding different types of photos with different colours of lip glosses,adding videos etc

Target Market(s)

All

Industry/Entity Type

Beauty industy

Coding

Coded - Design and coding required

Number of Pages Required

4 page

Requirements
Must have
• All payment options,easy to find,clear photos
Nice to have
• Photos of different ethnicity.Black,asian,white women

```html
<!DOCTYPE html>
<html lang="en">
<head>
<meta charset="utf-8">
<title>Glow With Mira — Lip Glosses</title>
<link href="https://fonts.googleapis.com/css2?family=Alegreya:wght@400;700&family=Lato:wght@400;700&display=swap" rel="stylesheet">
<style>
:root{
  --green:#234a1e;
  --green-dark:#1a3a16;
  --mint:#ecfbea;
  --bright:#0b8a0b;
  --subscribe:#1db34b;
  --ink:#2a2a2a;
  --muted:#444;
  --white:#fff;
  --line:#d9d9d9;
}
*{box-sizing:border-box;margin:0;padding:0}
html,body{width:1200px;height:4041px;overflow:hidden}
body{position:relative;font-family:'Lato',sans-serif;color:var(--ink);background:var(--white)}
.abs{position:absolute}
.serif{font-family:'Alegreya',serif}
.btn{position:absolute;display:flex;align-items:center;justify-content:center;background:var(--green);color:var(--white);font-weight:700;border-radius:30px;font-size:17px}

/* top bar & header */
.topbar{left:282px;top:0;width:918px;height:33px;background:var(--green);clip-path:polygon(0 0,100% 0,100% 100%,26px 100%);color:var(--white);font-size:14px}
.topbar span{position:absolute;top:8px;display:flex;align-items:center;gap:8px}
.brand-mark{left:110px;top:6px;width:150px;text-align:center}
.brand-mark .name{font-family:'Alegreya',serif;font-weight:700;font-size:15px;letter-spacing:2px;color:var(--green)}
.brand-mark .dot{width:56px;height:56px;border-radius:50%;background:var(--green);margin:6px auto 0}
.nav{top:61px;font-size:15px;color:var(--ink)}

/* hero */
.hero{left:0;top:110px;width:1200px;height:575px}
.hero-title{left:106px;top:220px;font-size:64px;font-weight:700;color:var(--white)}
.hero-sub{left:106px;top:310px;font-size:45px;color:var(--white)}
.hero-text{left:107px;top:392px;width:420px;font-size:15px;line-height:29px;color:var(--white)}

/* sections */
.h2{font-family:'Alegreya',serif;font-size:46px;color:var(--ink);white-space:nowrap}
.h2 b{color:var(--green)}
.center{left:0;width:1200px;text-align:center}
.para{font-size:15px;line-height:25px;color:var(--muted)}
.arrow{position:absolute;width:28px;height:28px}
.card{position:absolute;background:var(--white);border:2px solid var(--line);border-radius:6px;overflow:hidden}
.card .photo{position:absolute;left:0;top:0;width:100%}
.card .label{position:absolute;left:0;width:100%;text-align:center;font-size:21px;color:var(--ink)}
.qty{position:absolute;width:82px;height:28px;border:1px solid var(--line);border-radius:3px;display:flex;justify-content:space-around;align-items:center;font-size:18px}
.pname{position:absolute;font-size:25px;color:var(--ink)}
.price{position:absolute;font-size:25px;color:var(--ink)}

/* mailing */
.mailing{left:0;top:2568px;width:1200px;height:485px;background:linear-gradient(120deg,#2f3b1c 0%,#3e4a26 45%,#4a5a2e 70%,#2f4a2c 100%)}
.field{position:absolute;height:44px;background:var(--white);border-radius:4px;display:flex;align-items:center;gap:10px;padding-left:22px;font-size:14px;color:#777}

/* footer */
.footer{left:0;top:3656px;width:1200px;height:385px;background:var(--green);color:var(--white)}
.fh{position:absolute;font-size:20px;font-weight:700;color:var(--white)}
.fl{position:absolute;font-size:15px;color:var(--white);display:flex;align-items:center;gap:14px}
.fl i{width:8px;height:8px;border-radius:50%;background:var(--white);display:inline-block}
</style>
</head>
<body>

<!-- Header -->
<div class="abs topbar">
  <span style="left:38px"><svg width="18" height="18" viewBox="0 0 24 24" fill="#fff"><path d="M6.6 10.8a15 15 0 006.6 6.6l2.2-2.2a1 1 0 011-.25 11.4 11.4 0 003.6.57 1 1 0 011 1V20a1 1 0 01-1 1A17 17 0 013 4a1 1 0 011-1h3.5a1 1 0 011 1c0 1.25.2 2.45.57 3.57a1 1 0 01-.25 1z"/></svg>+1 555 014 2200</span>
  <span style="left:240px"><svg width="18" height="14" viewBox="0 0 24 18" fill="#fff"><path d="M0 0h24v18H0z" opacity=".0"/><path d="M1 1h22v16H1z" fill="none" stroke="#fff" stroke-width="2"/><path d="M1 1l11 9 11-9" fill="none" stroke="#fff" stroke-width="2"/></svg>info@glowwithmira.com</span>
  <span style="left:475px"><svg width="16" height="20" viewBox="0 0 24 30" fill="#fff"><path d="M12 0a10 10 0 00-10 10c0 8 10 20 10 20s10-12 10-20A10 10 0 0012 0zm0 14a4 4 0 110-8 4 4 0 010 8z"/></svg>22 Linden Avenue, Brooklyn, NY 11201</span>
</div>
<div class="abs brand-mark"><div class="name">GLOW WITH MIRA</div><div class="dot"></div></div>
<div class="abs nav" style="left:641px">Home</div>
<div class="abs nav" style="left:709px">About</div>
<div class="abs nav" style="left:778px">Products</div>
<div class="abs nav" style="left:866px">Shop</div>
<div class="btn" style="left:937px;top:50px;width:152px;height:47px">Contact Us</div>

<!-- Hero -->
<svg class="abs hero" viewBox="0 0 1200 575" aria-hidden="true">
  <defs>
    <linearGradient id="heroFill" x1="0" x2="1" y1="0" y2="0">
      <stop offset="0" stop-color="#060606"/><stop offset=".5" stop-color="#111"/><stop offset=".75" stop-color="#3a2418"/><stop offset="1" stop-color="#120c09"/>
    </linearGradient>
  </defs>
  <path d="M0 0H1200V520Q660 620 0 520Z" fill="url(#heroFill)"/>
  <path d="M0 520Q660 620 1200 520V532Q660 635 0 530Z" fill="var(--green)"/>
</svg>
<div class="abs" role="img" aria-label="Portrait of a woman with glossy lips and long dark hair" style="left:700px;top:110px;width:500px;height:500px"></div>
<div class="abs serif hero-title">Enhancing Beauty</div>
<div class="abs serif hero-sub">One Gloss at a Time</div>
<div class="abs hero-text">Unleash your natural glow with lip glosses designed to shine as bright as you do.</div>
<div class="btn" style="left:107px;top:478px;width:205px;height:48px">View Our Products</div>

<!-- Journey -->
<div class="abs" role="img" aria-label="Portrait of the founder in a magenta jacket" style="left:163px;top:766px;width:362px;height:362px;border-radius:50%;border:3px solid var(--green);background:linear-gradient(90deg,#6a3a5a 0%,#b03a9a 45%,#d9d9d6 70%,#eee 100%)"></div>
<div class="abs h2" style="left:643px;top:758px">My <b>Beauty Journey</b></div>
<div class="abs para" style="left:643px;top:842px;width:450px">Step into a world where beauty meets confidence. At Glow With Mira, we’re all about helping you feel empowered, radiant, and authentically YOU.</div>
<div class="abs para" style="left:643px;top:940px;width:450px">Whether you’re new to makeup or a beauty pro, our products are designed to bring out your natural glow and make you feel unstoppable.</div>
<div class="btn" style="left:643px;top:1048px;width:153px;height:47px">Read More</div>

<!-- Featured -->
<div class="abs" style="left:0;top:1210px;width:1200px;height:630px;background:var(--mint)"></div>
<div class="abs h2 center" style="top:1278px">Featured <b>Lip Glosses</b></div>
<div class="abs para center" style="top:1353px;left:230px;width:740px">Stay tuned for our collection of gorgeous lip glosses — perfect shine, nourishing feel, and made to enhance your natural beauty. More products to come!</div>
<svg class="arrow" style="left:38px;top:1583px" viewBox="0 0 28 28"><circle cx="14" cy="14" r="12.5" fill="none" stroke="#222" stroke-width="1.6"/><path d="M20 14H8m5-5l-5 5 5 5" fill="none" stroke="#222" stroke-width="1.6"/></svg>
<svg class="arrow" style="left:1136px;top:1583px" viewBox="0 0 28 28"><circle cx="14" cy="14" r="12.5" fill="none" stroke="#666" stroke-width="1.6"/><path d="M8 14h12m-5-5l5 5-5 5" fill="none" stroke="#666" stroke-width="1.6"/></svg>
<div class="card" style="left:110px;top:1439px;width:306px;height:315px">
  <div class="photo" role="img" aria-label="Black and white portrait with bold red lips" style="height:252px;background:linear-gradient(135deg,#1c1c1c,#7a7a7a 55%,#2a2a2a)"></div>
  <div class="label" style="top:270px">Luna</div>
</div>
<div class="card" style="left:447px;top:1439px;width:306px;height:315px">
  <div class="photo" role="img" aria-label="Portrait wearing a brown gloss and green top" style="height:252px;background:linear-gradient(180deg,#1a0f0a 0%,#5a3220 55%,#2fa35a 100%)"></div>
  <div class="label" style="top:270px">Plum Whisper</div>
</div>
<div class="card" style="left:783px;top:1439px;width:306px;height:315px">
  <div class="photo" role="img" aria-label="Close-up of lips with a bronze gloss" style="height:252px;background:radial-gradient(ellipse at 50% 55%,#c0783c 0%,#8a4d2a 45%,#5a3420 100%)"></div>
  <div class="label" style="top:270px">Golden Hour</div>
</div>

<!-- Products -->
<div class="abs h2 center" style="top:1911px">Our <b>Products</b></div>
<div class="abs para center" style="top:1985px;left:210px;width:780px">lick on the image for a full view and detailed information. Before adding to cart, please ensure you provide your shipping address in the "PROVIDE ORDER OR REQUEST DETAILS" field. All lip glosses are vegan, not tested on animals, and cruelty-free. PRICE INCLUDES SHIPPING</div>
<svg class="arrow" style="left:38px;top:2247px" viewBox="0 0 28 28"><circle cx="14" cy="14" r="12.5" fill="none" stroke="#222" stroke-width="1.6"/><path d="M20 14H8m5-5l-5 5 5 5" fill="none" stroke="#222" stroke-width="1.6"/></svg>
<svg class="arrow" style="left:1136px;top:2247px" viewBox="0 0 28 28"><circle cx="14" cy="14" r="12.5" fill="none" stroke="#666" stroke-width="1.6"/><path d="M8 14h12m-5-5l5 5-5 5" fill="none" stroke="#666" stroke-width="1.6"/></svg>

<div class="card" style="left:110px;top:2102px;width:306px;height:369px">
  <div class="photo" role="img" aria-label="Portrait with red lips on a light blue backdrop" style="height:252px;background:linear-gradient(90deg,#3a2218 0%,#7a4a34 50%,#b9d6e2 100%)"></div>
  <div class="pname" style="left:33px;top:264px">Luna</div>
  <div class="qty" style="left:210px;top:264px"><span>-</span><span>1</span><span>+</span></div>
  <div class="price" style="left:35px;top:314px">$31</div>
  <div class="btn" style="left:144px;top:303px;width:152px;height:46px">Add to Cart</div>
</div>
<div class="card" style="left:447px;top:2102px;width:306px;height:369px;border-color:var(--green-dark)">
  <div class="photo" role="img" aria-label="Two gloss tubes against a sunset sky" style="height:252px;background:linear-gradient(180deg,#e88a6a 0%,#f2a07a 45%,#b8a0b6 75%,#8fa2b8 100%)"></div>
  <div class="pname" style="left:21px;top:264px">Rose Flame</div>
  <div class="qty" style="left:212px;top:264px"><span>-</span><span>1</span><span>+</span></div>
  <div class="price" style="left:34px;top:314px">$31</div>
  <div class="btn" style="left:142px;top:302px;width:152px;height:46px">Shop Now</div>
</div>
<div class="card" style="left:783px;top:2102px;width:306px;height:369px">
  <div class="photo" role="img" aria-label="Close-up of lips with a deep wine gloss" style="height:252px;background:radial-gradient(ellipse at 50% 55%,#7a1a22 0%,#4a1a16 45%,#2a140e 100%)"></div>
  <div class="pname" style="left:30px;top:264px">Velvet Dusk</div>
  <div class="qty" style="left:213px;top:264px"><span>-</span><span>1</span><span>+</span></div>
  <div class="price" style="left:34px;top:314px">$31</div>
  <div class="btn" style="left:143px;top:303px;width:152px;height:46px">Add to Cart</div>
</div>

<!-- Mailing list -->
<div class="abs mailing" role="img" aria-label="Dimmed close-up of lips and a green lipstick tube"></div>
<div class="abs h2 center" style="top:2638px;color:var(--white)">Join the <b style="color:var(--white)">Mailing List</b></div>
<div class="abs center" style="top:2718px;font-size:16px;color:var(--white)">Be the first to know when new glosses drop, get exclusive discounts, and more!</div>
<div class="field" style="left:124px;top:2779px;width:446px"><svg width="14" height="14" viewBox="0 0 24 24" fill="#888"><circle cx="12" cy="7" r="5"/><path d="M2 24c0-6 4-9 10-9s10 3 10 9z"/></svg>First Name</div>
<div class="field" style="left:629px;top:2779px;width:446px"><svg width="14" height="14" viewBox="0 0 24 24" fill="#888"><circle cx="12" cy="7" r="5"/><path d="M2 24c0-6 4-9 10-9s10 3 10 9z"/></svg>Last Name</div>
<div class="field" style="left:124px;top:2848px;width:446px"><svg width="16" height="12" viewBox="0 0 24 18"><path d="M1 1h22v16H1z" fill="none" stroke="#888" stroke-width="2"/><path d="M1 1l11 9 11-9" fill="none" stroke="#888" stroke-width="2"/></svg>Email</div>
<div class="field" style="left:629px;top:2848px;width:446px"><svg width="14" height="14" viewBox="0 0 24 24" fill="#888"><path d="M6.6 10.8a15 15 0 006.6 6.6l2.2-2.2a1 1 0 011-.25 11.4 11.4 0 003.6.57 1 1 0 011 1V20a1 1 0 01-1 1A17 17 0 013 4a1 1 0 011-1h3.5a1 1 0 011 1c0 1.25.2 2.45.57 3.57a1 1 0 01-.25 1z"/></svg>Phone Number</div>
<div class="btn" style="left:494px;top:2920px;width:212px;height:48px;background:var(--bright);border:2px solid var(--white)">Submit</div>

<!-- Video -->
<div class="abs" role="img" aria-label="Video: applying red lipstick with a brush" style="left:111px;top:3133px;width:978px;height:433px;border-radius:6px;background:radial-gradient(ellipse at 50% 55%,#9a1e1e 0%,#7a2418 35%,#a0644a 70%,#6a3a28 100%)"></div>
<svg class="abs" style="left:976px;top:3163px" width="56" height="56" viewBox="0 0 56 56"><circle cx="28" cy="28" r="28" fill="#2a1a1a"/><path d="M22 17l17 11-17 11z" fill="#fff"/></svg>

<!-- Footer -->
<div class="abs footer"></div>
<div class="abs" style="left:112px;top:3735px;width:235px;text-align:center">
  <div class="serif" style="font-weight:700;font-size:21px;letter-spacing:3px;color:var(--white)">GLOW WITH MIRA</div>
  <div style="width:110px;height:110px;border-radius:50%;background:var(--white);margin:18px auto 0"></div>
</div>
<div class="abs" style="left:143px;top:3923px;display:flex;gap:15px">
  <span style="width:22px;height:22px;border-radius:50%;border:2px solid var(--white)"></span>
  <span style="width:22px;height:22px;border-radius:50%;border:2px solid var(--white)"></span>
  <span style="width:22px;height:22px;border-radius:50%;border:2px solid var(--white)"></span>
  <span style="width:22px;height:22px;border-radius:50%;border:2px solid var(--white)"></span>
</div>

<div class="fh" style="left:430px;top:3736px">Quick Links</div>
<div class="fl" style="left:432px;top:3785px"><i></i>Home</div>
<div class="fl" style="left:432px;top:3819px"><i></i>About Us</div>
<div class="fl" style="left:432px;top:3854px"><i></i>Products</div>
<div class="fl" style="left:432px;top:3888px"><i></i>Gallery</div>
<div class="fl" style="left:432px;top:3923px"><i></i>Shop</div>

<div class="fh" style="left:607px;top:3736px">Contact Us</div>
<div class="fl" style="left:605px;top:3785px;align-items:flex-start;width:230px;line-height:25px"><svg style="margin-top:4px;flex:none" width="16" height="18" viewBox="0 0 24 24" fill="#fff"><circle cx="12" cy="12" r="11"/><circle cx="12" cy="10" r="3.5" fill="var(--green)"/></svg><span>22 Linden Avenue,<br>Brooklyn, NY 11201</span></div>
<div class="fl" style="left:605px;top:3864px"><svg width="16" height="16" viewBox="0 0 24 24"><circle cx="12" cy="12" r="11" fill="#fff"/><path d="M6 8h12v8H6z" fill="var(--green)"/></svg>info@glowwithmira.com</div>
<div class="fl" style="left:605px;top:3908px"><svg width="16" height="16" viewBox="0 0 24 24"><circle cx="12" cy="12" r="11" fill="#fff"/><path d="M9 7l2 3-1.5 1.5a7 7 0 003 3L14 13l3 2-1 2c-4 0-9-5-9-9z" fill="var(--green)"/></svg>+1 555 014 2200</div>

<div class="fh" style="left:863px;top:3736px">Newsletter</div>
<div class="abs" style="left:867px;top:3783px;width:225px;font-size:14px;line-height:22px;color:var(--white)">Subscribe to our latest newsletter to get news about special discounts.</div>
<div class="abs" style="left:868px;top:3855px;width:221px;height:41px;background:var(--white);font-size:14px;color:#555;padding:12px 0 0 22px">Email</div>
<div class="abs" style="left:868px;top:3907px;width:119px;height:42px;background:var(--subscribe);color:var(--white);font-weight:700;font-size:17px;display:flex;align-items:center;justify-content:center">Subscribe</div>

<div class="abs" style="left:111px;top:3991px;width:978px;height:1px;background:rgba(255,255,255,.45)"></div>
<div class="abs center" style="top:4007px;font-size:14px;color:var(--white)">© 2025 Glow With Mira. All Rights Reserved.</div>

</body>
</html>
```